Exceptional Corporate Business Card Design

Hello,

We need an exceptional corporate business card design based on our logo attached. We require:

1. A Variation for letterpress print
2. Standard size of business card 84mm x 55mm (Artwork 88mm x 59mm)
3. Variation for square business card 65mm x 65mm (Artwork 69mm x 69mm)
4. Variation as a one side print
5. Adobe Illustrator files

The company is in the financial industry, talvenu.com

The logo is attached as vector pdf.
regards

```html
<!DOCTYPE html>
<html lang="en">
<head>
<meta charset="utf-8">
<title>Talvenu Business Card</title>
<link rel="stylesheet" href="https://fonts.googleapis.com/css2?family=Cinzel:wght@400;600;700&display=swap">
<style>
  :root {
    --bg: #e4e5e7;
    --ink-blue: #2e2b86;
    --deep-blue: #25236f;
    --mid-blue: #3a3890;
    --paper: #fbfbfa;
    --text-dark: #222233;
    --white: #ffffff;
  }
  * { margin: 0; padding: 0; box-sizing: border-box; }
  html, body {
    width: 1200px; height: 720px; overflow: hidden;
    background: var(--bg);
    font-family: "Cinzel", serif;
  }
  .stage {
    position: relative; width: 1200px; height: 720px;
  }
  .card {
    position: absolute; top: 242px;
    width: 420px; height: 240px;
    overflow: hidden;
  }
  /* Front */
  .card-front { left: 147px; background: var(--paper); }
  .portrait-panel {
    position: absolute; left: 0; top: 0; bottom: 0; width: 230px;
    background: radial-gradient(circle at 45% 50%, var(--mid-blue) 0%, var(--ink-blue) 55%, var(--deep-blue) 100%);
  }
  .front-brand {
    position: absolute; right: 14px; top: 22px;
    display: flex; align-items: center; gap: 6px;
    color: var(--ink-blue); font-weight: 600; font-size: 24px; letter-spacing: 0.5px;
  }
  .brand-dot {
    width: 30px; height: 30px; border-radius: 50%;
    background: var(--ink-blue);
  }
  .contact-block {
    position: absolute; right: 14px; text-align: right;
    color: var(--text-dark); font-size: 9.5px; line-height: 1.3;
  }
  .person { top: 94px; }
  .person-name { color: var(--ink-blue); font-weight: 700; font-size: 12.5px; }
  .person-role { font-size: 9px; }
  .address { top: 137px; font-size: 9.5px; }
  .contacts { top: 186px; }
  .contact-row {
    display: flex; justify-content: flex-end; align-items: center; gap: 6px;
    height: 12px;
  }
  .contact-row svg { width: 10px; height: 9px; fill: var(--ink-blue); }
  /* Back */
  .card-back {
    left: 633px;
    background: linear-gradient(160deg, #3c3a8c 0%, var(--ink-blue) 45%, var(--deep-blue) 100%);
  }
  .back-brand {
    position: absolute; inset: 0;
    display: flex; align-items: center; justify-content: center; gap: 10px;
    color: var(--white); font-weight: 600; font-size: 42px; letter-spacing: 1px;
  }
  .back-brand .brand-dot {
    width: 58px; height: 58px; background: var(--white);
  }
</style>
</head>
<body>
<main class="stage">
  <section class="card card-front">
    <div class="portrait-panel" role="img" aria-label="Engraved classical coin portrait illustration in deep blue"></div>

    <div class="front-brand"><span class="brand-dot"></span>TALVENU</div>

    <div class="contact-block person">
      <div class="person-name">Mara Eldin</div>
      <div class="person-role">Founder &amp; CEO</div>
    </div>

    <div class="contact-block address">
      <div>14-16 Harlow Lane,</div>
      <div>N3R 7QT, London, England</div>
    </div>

    <div class="contact-block contacts">
      <div class="contact-row">+44 1 55501234
        <svg viewBox="0 0 10 9"><path d="M1 3 Q5 0 9 3 L8 4 L6.5 3.5 L6.5 2.5 Q5 2 3.5 2.5 L3.5 3.5 L2 4 Z M2.5 4.5 H7.5 L8.5 8.5 H1.5 Z"/></svg>
      </div>
      <div class="contact-row">office@talvenu.com
        <svg viewBox="0 0 10 9"><path d="M0.5 1 H9.5 V8 H0.5 Z M1.3 1.8 L5 5 L8.7 1.8 Z" fill-rule="evenodd"/></svg>
      </div>
      <div class="contact-row">www.talvenu.com
        <svg viewBox="0 0 10 9"><path d="M0.5 0.5 H9.5 V6.5 H0.5 Z M1.5 1.5 V5.5 H8.5 V1.5 Z M4 7 H6 V7.8 H7.5 V8.6 H2.5 V7.8 H4 Z" fill-rule="evenodd"/></svg>
      </div>
    </div>
  </section>

  <section class="card card-back">
    <div class="back-brand"><span class="brand-dot"></span>TALVENU</div>
  </section>
</main>
</body>
</html>
```